Give my personal webpage more appeal!

I need my CV website improved - drmaraloftin.com.au.
I am using the template KESTIN from plovaworks. i would like to keep the already existing theme but am open to suggestions.
Please focus on imagery, colour scheme, and textures to enhance the appeal and look of the page.
The content is there, but now I need a designer to improve the look of my page.
I need styling, royalty-free unique modern images to make the page professional, personal and friendly.
I work in healthcare, so I'm a people person.
I teach professionals and I treat a lot of families.

Target Market(s)

Parents, Professional Healthcare providers

Number of Pages Required

1 page

Font styles to use
Serif
Sans Serif

Requirements
Must have
• My face - image at the top, all the information already contained in it.
• Links to the websites I manage such as my blog.
• One Page website.
• All the information it already contains with the ability to have more.
• Ideally, we would keep the same format for the page although I'm happy to expand column and change the page's structure with in the theme template KESTIN.
Nice to have
• The current KESTIN template. I would like to keep the already existing theme but am open to suggestions.
Should not have
• Multiple pages.

```html
<!DOCTYPE html>
<html lang="en">
<head>
<meta charset="utf-8">
<title>Dr Mara Loftin – Websites &amp; Contact</title>
<link rel="stylesheet" href="https://fonts.googleapis.com/css2?family=Montserrat:wght@400;700&family=Roboto:wght@400&family=Merriweather:wght@400&display=swap">
<style>
  :root {
    --coral: #ef4b5b;
    --panel: #f6f6f6;
    --field: #f4f4f4;
    --ink: #2f2f2f;
    --heading-grey: #6b6b6b;
    --body-grey: #555555;
    --logo-grey: #949494;
    --placeholder: #a3a3a3;
    --white: #ffffff;
  }
  * { box-sizing: border-box; margin: 0; padding: 0; }
  html, body { width: 1200px; height: 1000px; overflow: hidden; background: var(--white); }
  body { position: relative; font-family: "Montserrat", Arial, sans-serif; }

  .career-panel { position: absolute; left: 161px; top: 0; width: 1039px; height: 148px; background: var(--panel); }
  .career-panel__rule { position: absolute; left: 161px; top: 148px; width: 1039px; height: 7px; background: var(--coral); }
  .career-text {
    position: absolute; width: 175px;
    font-family: "Roboto", Arial, sans-serif; font-size: 8.6px; line-height: 14.6px; color: #666;
  }
  .career-text--left { left: 323px; top: 4px; }
  .career-text--right { left: 692px; top: -2px; width: 180px; }

  .websites__title {
    position: absolute; top: 204px; left: 0; width: 1342px; text-align: center;
    font-weight: 700; font-size: 18px; letter-spacing: 0.3px; color: var(--ink);
  }
  .site-link {
    position: absolute; display: flex; align-items: center; justify-content: center; gap: 8px;
    font-weight: 400; color: var(--logo-grey); text-decoration: none; text-align: center;
  }
  .site-link--blog { left: 297px; top: 285px; width: 175px; height: 85px; font-size: 26px; }
  .site-link--gut { left: 538px; top: 274px; width: 180px; height: 88px; font-size: 25px; background: #f1f1f1; }
  .site-link--reflex { left: 772px; top: 280px; width: 115px; height: 96px; font-size: 16px; line-height: 19px; flex-direction: column; }
  .site-link--learn { left: 915px; top: 278px; width: 155px; height: 102px; font-size: 20px; flex-direction: column; }
  .site-link__dot { width: 34px; height: 34px; border-radius: 50%; background: var(--logo-grey); }

  .social-band { position: absolute; left: 160px; top: 481px; width: 1040px; height: 64px; background: var(--coral); }
  .social-band__title { position: absolute; left: 108px; top: 22px; font-weight: 700; font-size: 19px; color: var(--white); }
  .social-link { position: absolute; top: 20px; display: flex; align-items: center; gap: 7px; color: var(--white); font-size: 13px; text-decoration: none; }
  .social-link--folk { left: 430px; }
  .social-link--work { left: 528px; }
  .social-link__dot { width: 22px; height: 22px; border-radius: 50%; background: var(--white); }

  .contact__title { position: absolute; left: 277px; top: 640px; font-weight: 700; font-size: 19.5px; color: var(--heading-grey); }
  .contact__line { position: absolute; left: 277px; font-size: 12px; line-height: 15px; color: var(--body-grey); }

  .note-form__field {
    position: absolute; background: var(--field);
    font-family: "Merriweather", Georgia, serif; font-size: 11.5px; color: var(--placeholder);
    padding: 16px 0 0 23px; text-transform: uppercase;
  }
  .note-form__field--name { left: 552px; top: 629px; width: 296px; height: 45px; }
  .note-form__field--phone { left: 552px; top: 683px; width: 296px; height: 44px; }
  .note-form__field--subject { left: 552px; top: 737px; width: 296px; height: 45px; }
  .note-form__field--message { left: 858px; top: 629px; width: 296px; height: 153px; }
  .note-form__send {
    position: absolute; left: 552px; top: 790px; width: 602px; height: 46px; background: var(--coral);
    color: var(--white); font-weight: 700; font-size: 18px; text-align: center; line-height: 46px; border-radius: 2px;
  }
</style>
</head>
<body>
  <section class="career-panel" aria-label="Career history"></section>
  <div class="career-panel__rule"></div>
  <p class="career-text career-text--left">train my Chiropractic Associates, Chiropractic Assistants and support staff. To keep the standards high, the team managed and motivated, and the clinic excelling.&nbsp; In July 2016 I sold this business but I continue to work here as an Associate Chiropractor.</p>
  <p class="career-text career-text--right">with those who ask, and how to life without expectations. He shaped me into the practitioner and teacher I have become.</p>

  <h2 class="websites__title">VISIT MY WEBSITES</h2>
  <a class="site-link site-link--blog" href="#">drMaras blog</a>
  <a class="site-link site-link--gut" href="#">GutwiseOZ</a>
  <a class="site-link site-link--reflex" href="#">Early Reflex Lab</a>
  <a class="site-link site-link--learn" href="#"><span class="site-link__dot"></span>learnMK.com.au</a>

  <section class="social-band">
    <h2 class="social-band__title">FIND ME ON SOCIAL MEDIA</h2>
    <a class="social-link social-link--folk" href="#"><span class="social-link__dot"></span>Folkbook</a>
    <a class="social-link social-link--work" href="#"><span class="social-link__dot"></span>Workline</a>
  </section>

  <h2 class="contact__title">CONTACT ME</h2>
  <p class="contact__line" style="top:680px">Wattle Grove<br>Brisbane, Australia</p>
  <p class="contact__line" style="top:725px">+61 3 80 00 41 17</p>
  <p class="contact__line" style="top:755px">info@drmaraloftin.au</p>

  <form class="note-form">
    <div class="note-form__field note-form__field--name">Name</div>
    <div class="note-form__field note-form__field--phone">Phone</div>
    <div class="note-form__field note-form__field--subject">Subject</div>
    <div class="note-form__field note-form__field--message">Your message</div>
    <div class="note-form__send">SEND ME A NOTE</div>
  </form>
</body>
</html>
```